An anniversary gift for my girlfriend

My girlfriend and I have been dating for almost 2 years. We met online and this has afforded us the really unique opportunity to have the first words we said to each other (the whole conversation, in fact) preserved. We're moving in together in a few months and she doesn't know that I saved the conversation. I've been waiting for this to turn it into something we can hang in our new place.

The only phrase I want to use is:
"Well if you dislike people's knees then I think we'll get along famously"

It's an Nobody Leaves Before Midnight in Portland reference for the curious.

I want the poster to use the words themselves as the art; I'm thinking typography. I'd like it to match her aesthetic, she likes to wear Nora Vell and T. Brisk. Colors shouldn't be anything too "girly". Somewhere I'd like to include the date June 1, 2015. It shouldn't be a major piece of the poster though, just a way to denote the date.

It should fit (and be fully visible in) a 16x20 (inches) frame

Thanks in advance for the work!

Requirements
Must have
• Must use only the words: "Well if you dislike people's knees then I think we'll get along famously"
• I want this to be typography, so making the phrase the center of the poster and the art itself.

```html
<!DOCTYPE html>
<html lang="en">
<head>
<meta charset="utf-8">
<title>Well — Anniversary Typographic Poster</title>
<link rel="stylesheet" href="https://fonts.googleapis.com/css2?family=Lobster+Two:ital,wght@1,700&family=Yanone+Kaffeesatz:wght@200;300&family=Montserrat:wght@800&family=Oswald:wght@300&family=Amatic+SC:wght@700&family=Playfair+Display:ital,wght@1,900&family=Indie+Flower&family=Abril+Fatface&display=swap">
<style>
  :root {
    --poster-bg: #7fe1d4;
    --ink: #ffffff;
  }
  html, body {
    margin: 0;
    padding: 0;
    width: 960px;
    height: 1200px;
    overflow: hidden;
    background: var(--poster-bg);
  }
  .poster {
    position: relative;
    width: 960px;
    height: 1200px;
    background: var(--poster-bg);
    color: var(--ink);
  }
  .phrase { margin: 0; font-weight: normal; }
  .phrase span { position: absolute; white-space: nowrap; line-height: 1; }

  .word-well {
    left: 234px; top: 166px;
    font-family: "Lobster Two", cursive;
    font-style: italic; font-weight: 700;
    font-size: 280px; letter-spacing: -6px;
  }
  .word-if-you {
    left: 272px; top: 445px;
    font-family: "Yanone Kaffeesatz", sans-serif;
    font-weight: 200; font-size: 86px; letter-spacing: 1px;
  }
  .word-dislike {
    left: 462px; top: 437px;
    font-family: "Lobster Two", cursive;
    font-style: italic; font-weight: 700; font-size: 84px;
  }
  .word-peoples {
    left: 299px; top: 526px;
    font-family: "Montserrat", sans-serif;
    font-weight: 800; font-size: 68px; letter-spacing: 0;
  }
  .word-knees {
    left: 293px; top: 589px;
    font-family: "Amatic SC", sans-serif;
    font-weight: 700; font-size: 160px; letter-spacing: -2px;
    transform: scaleX(0.77);
    transform-origin: left top;
  }
  .word-then {
    left: 506px; top: 616px;
    font-family: "Oswald", sans-serif;
    font-weight: 300; font-size: 56px;
  }
  .word-i-think {
    left: 502px; top: 678px;
    font-family: "Playfair Display", serif;
    font-style: italic; font-weight: 900; font-size: 44px;
  }
  .word-get-along {
    left: 310px; top: 742px;
    font-family: "Indie Flower", cursive;
    font-size: 57px;
  }
  .word-famously {
    left: 311px; top: 800px;
    font-family: "Abril Fatface", serif;
    font-size: 71px;
  }
  .date {
    position: absolute;
    left: 0; right: 0; top: 985px;
    margin: 0;
    padding-right: 6px;
    text-align: center;
    font-family: "Yanone Kaffeesatz", sans-serif;
    font-weight: 300; font-size: 38px; letter-spacing: 1px;
  }
</style>
</head>
<body>
  <main class="poster">
    <h1 class="phrase">
      <span class="word-well">Well</span>
      <span class="word-if-you">IF YOU</span>
      <span class="word-dislike">dislike</span>
      <span class="word-peoples">PEOPLE'S</span>
      <span class="word-knees">KNEES</span>
      <span class="word-then">THEN</span>
      <span class="word-i-think">i think</span>
      <span class="word-get-along">we'll get along</span>
      <span class="word-famously">famously.</span>
    </h1>
    <p class="date">06.01.2015</p>
  </main>
</body>
</html>
```